Flyer Template Design

I have attached 4 files. I would like a design template that could be used across these documents so that they have a common look and feel. The content of the documents is tested and should not be changed significantly. The images can be changed. I have also attache our logo for color compatibility.
Updates

Need extra days to review

Target Market(s)

Wealthy Christian donors

Font styles to use
Serif
Sans Serif

```html
<!DOCTYPE html>
<html lang="en">
<head>
<meta charset="utf-8">
<title>Hastening His Coming</title>
<link rel="stylesheet" href="https://fonts.googleapis.com/css2?family=Roboto+Slab:wght@300;700&family=Lato:ital,wght@0,400;0,700&family=Playfair+Display:ital,wght@0,400;0,700;1,400&display=swap">
<style>
  :root {
    --backdrop: #d6d6d6;
    --paper: #ffffff;
    --navy: #0f4a78;
    --heading-blue: #1d4f7c;
    --sky: #5cc8f0;
    --text-grey: #555a5f;
    --night-top: #0d3a6e;
    --night-bottom: #0a1c3c;
    --white: #ffffff;
  }
  * { margin: 0; padding: 0; box-sizing: border-box; }
  html, body {
    width: 902px; height: 1200px; overflow: hidden;
    background: var(--backdrop);
  }
  .flyer {
    position: absolute; left: 69px; top: 59px;
    width: 766px; height: 1082px;
    background: var(--paper); overflow: hidden;
    font-family: "Lato", sans-serif; color: var(--text-grey);
  }
  .title-band {
    position: absolute; left: 0; top: 89px; width: 346px; height: 100px;
    background: linear-gradient(90deg, #0d4b7d 0%, #3c8fc4 55%, #62cdf3 100%);
  }
  .title { position: absolute; left: 383px; top: 86px; }
  .title-strong {
    display: block; font-family: "Roboto Slab", serif; font-weight: 700;
    font-size: 41px; line-height: 46px; color: var(--navy); letter-spacing: 0.5px;
  }
  .title-light {
    display: block; font-family: "Roboto Slab", serif; font-weight: 300;
    font-size: 52px; line-height: 58px; color: var(--sky); margin-top: 4px;
  }
  .intro {
    position: absolute; left: 88px; top: 210px; width: 620px;
    font-size: 13.4px; line-height: 22px;
  }
  .intro strong { color: var(--navy); font-weight: 700; }
  .forest-photo {
    position: absolute; left: 86px; top: 292px; width: 260px; height: 286px;
    background: radial-gradient(circle at 50% 45%, #b7dc6a 0%, #6aa83a 40%, #2f5a1e 75%, #1c3512 100%);
  }
  .scripture { position: absolute; left: 363px; top: 299px; width: 350px; }
  .scripture h2, .scripture h3 {
    font-family: "Playfair Display", serif; font-weight: 400; color: var(--heading-blue);
  }
  .scripture h2 { font-size: 15px; line-height: 20px; margin-bottom: 10px; }
  .scripture h3 { font-size: 15.5px; line-height: 19px; margin-bottom: 5px; }
  .scripture p { font-size: 10.8px; line-height: 14px; margin-bottom: 10px; }
  .scripture .wide { margin-left: 2px; }
  .closing-question {
    position: absolute; left: 86px; top: 597px;
    font-family: "Playfair Display", serif; font-size: 15.5px; color: var(--heading-blue);
  }
  .night-section {
    position: absolute; left: 0; top: 638px; width: 766px; height: 444px;
    background: linear-gradient(180deg, var(--night-top) 0%, #143f78 45%, #112e5e 75%, var(--night-bottom) 100%);
  }
  .section-frame { position: absolute; left: 69px; top: 638px; }
  .section-label {
    position: absolute; left: 88px; top: 685px;
    font-family: "Playfair Display", serif; font-weight: 700; font-size: 15px;
    color: var(--white); letter-spacing: 0.2px;
  }
  .night-copy {
    position: absolute; left: 86px; width: 622px;
    font-size: 11.2px; line-height: 14px; color: var(--white);
  }
  .copy-one { top: 768px; }
  .copy-two { top: 892px; }
  .call-out {
    position: absolute; left: 86px; top: 838px;
    font-family: "Playfair Display", serif; font-weight: 700; font-size: 27px; color: var(--white);
  }
  .invitation {
    position: absolute; left: 85px; top: 948px;
    font-family: "Playfair Display", serif; font-style: italic; font-size: 19px; color: var(--white);
  }
</style>
</head>
<body>
<article class="flyer">
  <div class="title-band"></div>
  <h1 class="title">
    <span class="title-strong">HASTENING</span>
    <span class="title-light">HIS COMING</span>
  </h1>

  <p class="intro">In his second letter, the Apostle Peter asks, what kind of people should believers be?<br>
    <strong>He answers</strong>, “We ought to live holy and godly lives, looking for and hastening the coming<br>
    of the day of God.” But how can we do that? How is it possible to hasten the coming of that day?</p>

  <div class="forest-photo" role="img" aria-label="Photo of a person standing beneath a green forest canopy"></div>

  <section class="scripture">
    <h2>“AND THEN THE END WILL COME”</h2>
    <p>When Jesus’ disciples asked Him, Tell us, what will be the sign of your coming and of the end of the age?</p>
    <h3>He replied,</h3>
    <p>This gospel of the kingdom will be preached in the whole world as a testimony to all nations, and then the end will come.”</p>
    <h3>When will Jesus return? He said, only after gospel has been preached to “all nations.”</h3>
    <p class="wide">In the Bible, the word “nations” refers to people groups: groups of people with common ethnicity, culture, and language. Amazingly, there are about 12,000 of these “nations” around the world—and Jesus commanded His church to preach the gospel to all of them! Today, there are still 500 people groups without a single believer. No one has ever gone to these remaining “unengaged” groups with the gospel. They do not know the name of Jesus.</p>
  </section>

  <p class="closing-question">After 2000 years, isn’t it time that they all heard?</p>

  <div class="night-section" role="img" aria-label="Blue-toned photo of a person on a wooden lookout under tree branches at dusk"></div>
  <svg class="section-frame" width="100" height="94" viewBox="0 0 100 94" aria-hidden="true">
    <polyline points="1,0 1,91 88,91" fill="none" stroke="#ffffff" stroke-width="1.2"/>
    <rect x="85" y="87" width="7" height="7" fill="#ffffff"/>
  </svg>
  <h2 class="section-label">COMPLETING THE CALL</h2>

  <p class="night-copy copy-one">So how can we “hasten the coming of the day of God?” By completing the work Jesus gave us to do! Jesus said He would not return until the gospel is preached to every nation, so that’s what we need to do: take the gospel to all the groups that have never once heard it. Fortunately, we now know who these last groups are and where they are located, by God’s grace it is possible that we can engage all of them with the gospel within the next 3 years.</p>

  <p class="call-out">You can make that happen.</p>

  <p class="night-copy copy-two">Partner with the Harvest Reach Fund and finance the missionaries who are taking the gospel for the first time to those last remaining people groups. Your investment will “hastening the coming of the day of God” by accelerating the effort to make “disciples in every nation.” In 2018, our partners helped take the gospel to 231 people groups in 35 countries.</p>

  <p class="invitation">Join us as we invest to make disciples in “all nations” by 2022.</p>
</article>
</body>
</html>
```